Kivo Commercial Cleaning is lookong for a new business card design.

A fresh new design that's professional and stylish. We need a serious upgrade to our business cards. I have included pictures of our existing ones. Our clients include professional individuals and business owners. We woupdblike something professional and upbeat. Please have fun and see what you come uo with.

Target Market(s)

Property managers, business owners, facility managers and other similar professionals

Industry/Entity Type

Janitorial

Contact Information for Business Card

Name, cell, office number, email, web address

Font styles to use
Sans Serif

Colors

Designer to choose colors to be used in the design.

Requirements
Must have
• please use the green color in our logo
Nice to have
• Bar code
Should not have
• Address

```html
<!DOCTYPE html>
<html lang="en">
<head>
<meta charset="utf-8">
<title>Kivo Commercial Cleaning – Business Card</title>
<link rel="stylesheet" href="https://fonts.googleapis.com/css2?family=Fredoka:wght@500;600&family=Arimo:wght@400&display=swap">
<style>
  :root {
    --bg: #141414;
    --card: #2a2a2b;
    --green: #37b34a;
    --blue: #3e6db5;
    --white: #f4f4f4;
    --emboss: #1a1a1a;
  }
  * { margin: 0; padding: 0; box-sizing: border-box; }
  html, body { width: 1200px; height: 963px; overflow: hidden; background: var(--bg); }
  .canvas {
    width: 1200px; height: 963px;
    display: flex; flex-direction: column; align-items: center; justify-content: center;
    gap: 70px;
  }
  .card {
    position: relative;
    width: 620px; height: 354px;
    background: var(--card);
    border-radius: 20px;
    border-right: 3px solid var(--green);
    border-bottom: 3px solid var(--green);
    overflow: hidden;
    font-family: "Fredoka", sans-serif;
  }
  /* front */
  .brand {
    position: absolute; left: 300px; top: 40px;
    color: var(--green);
    font-weight: 600; font-size: 130px; line-height: 1;
    letter-spacing: -2px;
  }
  .brand-sub {
    position: absolute; left: 250px; top: 178px;
    color: var(--blue);
    font-weight: 500; font-size: 24px;
  }
  .holder {
    position: absolute; left: 40px; width: 232px; top: 238px;
    text-align: right;
    color: var(--green);
    font-weight: 600; font-size: 30px;
  }
  .divider {
    position: absolute; left: 292px; top: 232px;
    width: 2px; height: 86px; background: var(--green);
  }
  .contact {
    position: absolute; left: 312px; top: 234px;
    list-style: none;
    font-family: "Arimo", sans-serif; font-size: 18px; color: var(--white);
  }
  .contact li { display: flex; align-items: center; gap: 10px; height: 28px; }
  .contact svg { width: 16px; height: 16px; flex: none; }
  /* back */
  .brand-emboss {
    position: absolute; left: 0; right: 0; top: 70px;
    text-align: center;
    color: var(--emboss);
    font-weight: 600; font-size: 170px; line-height: 1;
    letter-spacing: -3px;
  }
  .tagline {
    position: absolute; left: 0; right: 0; top: 270px;
    text-align: center;
    color: var(--green);
    font-family: "Arimo", sans-serif; font-size: 26px;
  }
</style>
</head>
<body>
<main class="canvas">
  <section class="card card-front">
    <div class="brand">kivo</div>
    <div class="brand-sub">commercial cleaning</div>
    <div class="holder">maren ostrova</div>
    <div class="divider"></div>
    <ul class="contact">
      <li>
        <svg viewBox="0 0 16 16" aria-hidden="true"><path d="M4 1.5l2.2 2.6-1.3 1.6c.9 2 2.4 3.5 4.4 4.4l1.6-1.3 2.6 2.2-1.4 2.2C7 12.6 3.4 9 1.8 3L4 1.5z" fill="var(--green)"/></svg>
        (555) 014-2273
      </li>
      <li>
        <svg viewBox="0 0 16 16" aria-hidden="true"><rect x="1.5" y="3.5" width="13" height="9" rx="1" fill="none" stroke="var(--green)" stroke-width="1.4"/><path d="M1.8 4l6.2 5 6.2-5" fill="none" stroke="var(--green)" stroke-width="1.4"/></svg>
        maren@kivocleaning.com
      </li>
      <li>
        <svg viewBox="0 0 16 16" aria-hidden="true"><circle cx="8" cy="8" r="6.5" fill="none" stroke="var(--green)" stroke-width="1.3"/><ellipse cx="8" cy="8" rx="2.8" ry="6.5" fill="none" stroke="var(--green)" stroke-width="1.1"/><path d="M1.5 8h13M2.6 4.6h10.8M2.6 11.4h10.8" stroke="var(--green)" stroke-width="1.1"/></svg>
        www.kivocleaning.com
      </li>
    </ul>
  </section>

  <section class="card card-back">
    <div class="brand-emboss">kivo</div>
    <div class="tagline">clean spaces, happy places</div>
  </section>
</main>
</body>
</html>
```